Marlow Hire Business Card for recruitment company

We are looking for a Business Card Design that incorporates our personal details and our busines name and logo. We are a specialized search consultancy that recruit Property and Construction professionals.
We would like a business card that stands out and is appealing to the Construction and Property industry as well.

Target Market(s)

people in the construction and property industry

Contact Information for Business Card

Business Name and logo

Font styles to use
Serif

Colors
0094D4
00A9DD
6FCCEA
C7EBF8
E9F6FB

Requirements
Must have
• Business name and logo as well as contact details
Should not have
• No photos of us please

```html
<!DOCTYPE html>
<html lang="en">
<head>
<meta charset="utf-8">
<title>Marlow Hire Business Card</title>
<link rel="stylesheet" href="https://fonts.googleapis.com/css2?family=Crimson+Text:wght@400;600&display=swap">
<style>
  :root {
    --backdrop: #5c5c5c;
    --card-blue: #2fa5dc;
    --brand-deep: #0094d4;
    --ink-white: #ffffff;
    --ink-soft: #e9f6fb;
    --icon-fill: #c7ebf8;
    --icon-glyph: #0094d4;
  }
  * { box-sizing: border-box; margin: 0; padding: 0; }
  html, body {
    width: 1200px; height: 899px; overflow: hidden;
    background: var(--backdrop);
    font-family: "Crimson Text", Georgia, serif;
  }
  .stage {
    position: relative; width: 1200px; height: 899px;
    display: flex; flex-direction: column; align-items: center; justify-content: center; gap: 44px;
  }
  .card {
    position: relative; width: 560px; height: 320px;
    background: var(--card-blue);
    color: var(--ink-white);
    box-shadow: 0 10px 24px rgba(0,0,0,0.35);
  }
  /* front */
  .card-front { display: flex; }
  .identity {
    width: 52%; display: flex; flex-direction: column; justify-content: center; align-items: flex-end;
    padding-right: 30px; text-align: right;
  }
  .brand-name {
    font-size: 30px; font-weight: 400; letter-spacing: 3px; text-transform: uppercase; line-height: 1;
  }
  .person-name {
    margin-top: 14px; font-size: 18px; letter-spacing: 1.5px; text-transform: uppercase;
  }
  .person-role {
    font-size: 15px; padding-bottom: 3px; border-bottom: 1px solid var(--ink-white);
  }
  .divider {
    width: 1px; background: var(--ink-white); margin: 48px 0; opacity: 0.9;
  }
  .contacts {
    flex: 1; display: flex; flex-direction: column; justify-content: center; gap: 12px; padding: 0 26px;
    list-style: none;
  }
  .contact-item {
    display: flex; align-items: center; justify-content: flex-end; gap: 10px;
    font-size: 14px; line-height: 1.2; text-align: right; color: var(--ink-soft);
  }
  .contact-icon {
    flex: none; width: 18px; height: 18px; border-radius: 50%; background: var(--icon-fill);
    display: flex; align-items: center; justify-content: center;
  }
  .contact-icon svg { width: 11px; height: 11px; fill: var(--icon-glyph); }
  .contact-gap { margin-top: 10px; }
  /* back */
  .card-back { display: flex; align-items: center; justify-content: center; }
  .card-back .brand-name { font-size: 38px; letter-spacing: 4px; }
</style>
</head>
<body>
<main class="stage">
  <section class="card card-front" aria-label="Business card front">
    <div class="identity">
      <p class="brand-name">Marlow Hire</p>
      <p class="person-name">Daniel R. Whitcombe</p>
      <p class="person-role">Managing Director</p>
    </div>
    <div class="divider"></div>
    <ul class="contacts">
      <li class="contact-item">
        <span>2170 Harbor Crescent<br>Alexandria, VA 22314</span>
        <span class="contact-icon"><svg viewBox="0 0 12 12"><path d="M6 0.5a4 4 0 0 0-4 4c0 3 4 7 4 7s4-4 4-7a4 4 0 0 0-4-4zm0 5.6a1.6 1.6 0 1 1 0-3.2 1.6 1.6 0 0 1 0 3.2z"/></svg></span>
      </li>
      <li class="contact-item">
        <span>+1 703 555 0148</span>
        <span class="contact-icon"><svg viewBox="0 0 12 12"><path d="M2.4 1l2 .2 1 2.6-1.3 1a6.5 6.5 0 0 0 3.1 3.1l1-1.3 2.6 1 .2 2c0 .6-.5 1.2-1.2 1.2A9.8 9.8 0 0 1 1.2 2.2C1.2 1.5 1.8 1 2.4 1z"/></svg></span>
      </li>
      <li class="contact-item contact-gap">
        <span>hello@marlowhire.com</span>
        <span class="contact-icon"><svg viewBox="0 0 12 12"><path d="M1 2.5h10v7H1z M1.5 3l4.5 3.5L10.5 3" fill="none" stroke="#0094d4" stroke-width="1.2"/></svg></span>
      </li>
      <li class="contact-item">
        <span>www.marlowhire.com</span>
        <span class="contact-icon"><svg viewBox="0 0 12 12"><path d="M2 1.5l8.5 4-3.6 1.2-1.3 3.8z"/></svg></span>
      </li>
    </ul>
  </section>

  <section class="card card-back" aria-label="Business card back">
    <p class="brand-name">Marlow Hire</p>
  </section>
</main>
</body>
</html>
```